Wine Label Needed

We need a front and back wine label design for our new winery based out of Berks County, PA. We love designs using typography as a main element. We also need this done very quickly. I will have a higher resolution logo available to provide the winner with. The jpg attached labeled Vineyards is a stock image I purchased that can be included on the back of the label, possibly. Thanks so much!
Updates

Here are some additional inspirational ideas I came across: https://typebazaar.example/KorvenDaly/41927-Pellow-Glyph-Bundle-62OFF https://typebazaar.example/Mirabeth/38214-Quarry-Stone-Lettering-Extras https://typebazaar.example/tovigrune/42871-Velmora-Lettering

I've uploaded the design board to our restaurant that we'll be selling the wine in so you can get an overall feel of the look of the business. Hope this helps!

Reason: Sorry for the extension, but I didn't plan this out very well since I leave for vacation Monday - Friday and need more time to look over all these fabulous submissions! Thanks for your understanding!

Just got back from vacation and will be looking over everyone's beautiful designs today! Thanks so much for your patience!

Target Market(s)

Younger crowd

Font styles to use
Serif
Decorative
Script

Requirements
Must have
• Must say 750 ml
Must have a vintage date listed of 2013
Use an example wine name, i.e. cabernet sauvignon
The back will have a description of the wine which I can provide at a later date and also the standard government warning. It will also need space for a bar code. The back must also say: Cellared and Bottled by Tressaly Estate Winery. Also must say: Contains Sulfites
Nice to have
• On the inspiration image attached for the can called Pebbleton, I love the typography that's used to describe the beverage. Could possibly do something like this, but we don't have descriptors of our wines just yet.

```html
<!DOCTYPE html>
<html lang="en">
<head>
<meta charset="utf-8">
<title>Tressaly Estate Winery – Cabernet Sauvignon Labels</title>
<link rel="stylesheet" href="https://fonts.googleapis.com/css2?family=Cinzel:wght@400;700&family=Pinyon+Script&family=Special+Elite&family=Josefin+Slab:wght@600;700&display=swap">
<style>
  :root {
    --paper: #e8dcbd;
    --paper-light: #efe6cc;
    --paper-dark: #d6c59c;
    --ink: #2b2219;
    --ink-soft: #4a3d2e;
    --vine-green: #5d7b2f;
    --stage: #ffffff;
  }
  * { box-sizing: border-box; margin: 0; padding: 0; }
  html, body { width: 814px; height: 1200px; overflow: hidden; background: var(--stage); }
  .canvas { position: relative; width: 814px; height: 1200px; }

  /* Neck strips */
  .neck-strip {
    position: absolute; top: 90px; width: 74px; height: 250px;
    background: var(--paper);
    clip-path: polygon(0 0, 100% 0, 100% 100%, 50% 90%, 0 100%);
  }
  .neck-strip .neck-pattern {
    position: absolute; inset: 0;
    background: linear-gradient(180deg, var(--paper-dark), var(--paper) 45%, var(--paper-dark));
  }
  .neck-strip .neck-seal {
    position: absolute; left: 5px; top: 110px; width: 64px; height: 64px;
    border-radius: 50%; background: var(--paper-light);
    border: 2px solid var(--ink);
    display: flex; align-items: center; justify-content: center;
    font-family: 'Cinzel', serif; font-size: 9px; font-weight: 700; color: var(--ink);
    letter-spacing: 0.5px;
  }
  .neck-front { left: 173px; }
  .neck-back { left: 572px; }

  /* Front label */
  .front-label {
    position: absolute; left: 40px; top: 390px; width: 340px; height: 560px;
    background: var(--paper);
    box-shadow: inset 0 0 40px rgba(120, 95, 50, 0.35);
    overflow: hidden;
  }
  .front-label .flourish-field {
    position: absolute; left: 0; right: 0; top: 92px; bottom: 0;
    background: radial-gradient(circle at 50% 55%, var(--paper-light) 0 30%, #b9a57d 60%, #8a7758 100%);
    opacity: 0.85;
  }
  .brand-cartouche {
    position: absolute; left: 50%; top: 0; transform: translateX(-50%);
    width: 250px; height: 112px;
    background: var(--paper-light);
    border: 1.5px solid var(--ink);
    border-top: none;
    border-radius: 0 0 40px 40px;
    text-align: center; padding-top: 22px;
  }
  .brand-name {
    font-family: 'Cinzel', serif; font-size: 22px; font-weight: 400; color: var(--ink);
    letter-spacing: 1px; line-height: 1;
  }
  .brand-sub {
    font-family: 'Cinzel', serif; font-size: 9px; color: var(--ink); letter-spacing: 2px; margin-top: 5px;
  }
  .brand-motto {
    font-family: 'Pinyon Script', cursive; font-size: 17px; color: var(--vine-green); margin-top: 3px;
  }
  .varietal-medallion {
    position: absolute; left: 50%; top: 200px; transform: translateX(-50%);
    width: 240px; height: 240px; border-radius: 50%;
    background: var(--paper-light);
    border: 2px solid var(--ink);
    box-shadow: 0 0 0 4px var(--paper-light), 0 0 0 5px var(--ink);
    overflow: hidden; text-align: center;
  }
  .varietal-name {
    font-family: 'Cinzel', serif; font-weight: 700; font-size: 32px; line-height: 1.02;
    color: var(--ink); margin-top: 42px; letter-spacing: 0.5px;
  }
  .volume {
    font-family: 'Cinzel', serif; font-size: 10px; color: var(--ink); letter-spacing: 1px;
    margin-top: 6px; border-top: 1px solid var(--ink); display: inline-block; padding: 1px 10px 0;
  }
  .vineyard-view {
    position: absolute; left: 0; right: 0; bottom: 0; height: 100px;
    background: linear-gradient(180deg, #cdbd98 0%, #6f604a 100%);
  }
  .vintage-seal {
    position: absolute; left: 50%; top: 448px; transform: translateX(-50%);
    width: 50px; height: 50px; border-radius: 50%;
    background: var(--paper-light); border: 1.5px solid var(--ink);
    display: flex; align-items: center; justify-content: center;
    font-family: 'Cinzel', serif; font-size: 13px; color: var(--ink);
  }

  /* Back label */
  .back-label { position: absolute; left: 444px; top: 400px; width: 330px; height: 530px; }
  .back-label svg { position: absolute; inset: 0; }
  .back-label .cluster-body { fill: var(--paper); }
  .back-label .bubble-ring { fill: var(--paper-light); stroke: var(--ink-soft); stroke-width: 1; }
  .back-label .bubble-ring.dashed { stroke-dasharray: 3 3; }
  .scroll-ornament {
    position: absolute; left: 40px; top: 18px; width: 250px; height: 80px;
    background: linear-gradient(90deg, var(--paper), #a89570 50%, var(--paper));
    opacity: 0.6; border-radius: 40px;
  }
  .bubble {
    position: absolute; display: flex; flex-direction: column; align-items: center; justify-content: center;
    text-align: center; color: var(--ink); transform: translate(-50%, -50%);
  }
  .typewriter { font-family: 'Special Elite', monospace; text-transform: uppercase; }
  .slab { font-family: 'Josefin Slab', serif; font-weight: 700; }
  .script { font-family: 'Pinyon Script', cursive; }
  .b-king { left: 45px; top: 150px; width: 56px; font-size: 7px; line-height: 1.3; }
  .b-grape { left: 165px; top: 150px; width: 100px; font-size: 17px; line-height: 1; text-transform: lowercase; }
  .b-vintage { left: 280px; top: 157px; width: 84px; }
  .b-vintage .label { font-size: 8px; }
  .b-vintage .year { font-size: 26px; line-height: 1; border-top: 1px solid var(--ink); border-bottom: 1px solid var(--ink); padding: 1px 4px; margin: 2px 0; }
  .b-vintage .note { font-size: 6px; }
  .b-sulfites { left: 55px; top: 232px; width: 74px; font-size: 19px; line-height: 1; }
  .b-cellared { left: 170px; top: 265px; width: 100px; font-size: 9px; line-height: 1.35; }
  .b-alc { left: 275px; top: 262px; width: 64px; }
  .b-alc .label { font-size: 8px; }
  .b-alc .value { font-size: 15px; border-top: 1px solid var(--ink); border-bottom: 1px solid var(--ink); }
  .b-alc .note { font-size: 5px; }
  .b-motto { left: 90px; top: 302px; width: 50px; font-size: 10px; line-height: 1; }
  .b-pairing { left: 130px; top: 372px; width: 88px; font-family: 'Special Elite', monospace; font-size: 6.5px; line-height: 1.3; }
  .b-fact { left: 240px; top: 362px; width: 90px; font-size: 7.5px; line-height: 1.3; }
</style>
</head>
<body>
<main class="canvas">

  <!-- Neck strips -->
  <div class="neck-strip neck-front">
    <div class="neck-pattern" role="img" aria-label="Engraved grape cluster and leaf flourish pattern"></div>
    <div class="neck-seal">Tressaly</div>
  </div>
  <div class="neck-strip neck-back">
    <div class="neck-pattern" role="img" aria-label="Engraved grape cluster and leaf flourish pattern"></div>
    <div class="neck-seal">Tressaly</div>
  </div>

  <!-- Front label -->
  <section class="front-label">
    <div class="flourish-field" role="img" aria-label="Engraved baroque leaf scrolls and grape clusters surrounding the central medallion"></div>
    <header class="brand-cartouche">
      <div class="brand-name">TRESSALY ESTATE</div>
      <div class="brand-sub">WINERY</div>
      <div class="brand-motto">Nel Vino C'è la Verità</div>
    </header>
    <div class="varietal-medallion">
      <h1 class="varietal-name">CABERNET<br>SAUVIGNON</h1>
      <div class="volume">750 ML</div>
      <div class="vineyard-view" role="img" aria-label="Engraved vineyard rows stretching to the horizon"></div>
    </div>
    <div class="vintage-seal">2013</div>
  </section>

  <!-- Back label -->
  <section class="back-label">
    <svg width="330" height="530" viewBox="0 0 330 530" aria-hidden="true">
      <path class="cluster-body" d="M10,115 C0,60 40,40 72,52 C92,12 132,2 165,22 C198,2 238,12 258,52 C290,40 330,60 320,115 Z"/>
      <circle class="cluster-body" cx="60" cy="135" r="55"/>
      <circle class="cluster-body" cx="270" cy="135" r="55"/>
      <circle class="cluster-body" cx="165" cy="175" r="85"/>
      <circle class="cluster-body" cx="60" cy="235" r="50"/>
      <circle class="cluster-body" cx="275" cy="240" r="55"/>
      <circle class="cluster-body" cx="170" cy="290" r="90"/>
      <circle class="cluster-body" cx="90" cy="305" r="38"/>
      <circle class="cluster-body" cx="135" cy="370" r="60"/>
      <circle class="cluster-body" cx="240" cy="360" r="62"/>
      <circle class="cluster-body" cx="180" cy="420" r="60"/>
      <circle class="cluster-body" cx="178" cy="470" r="50"/>

      <circle class="bubble-ring" cx="45" cy="150" r="32"/>
      <circle class="bubble-ring dashed" cx="165" cy="150" r="55"/>
      <circle class="bubble-ring" cx="280" cy="157" r="45"/>
      <circle class="bubble-ring" cx="55" cy="232" r="40"/>
      <circle class="bubble-ring" cx="170" cy="265" r="58"/>
      <circle class="bubble-ring" cx="275" cy="262" r="38"/>
      <circle class="bubble-ring" cx="90" cy="302" r="28"/>
      <circle class="bubble-ring" cx="130" cy="372" r="50"/>
      <circle class="bubble-ring" cx="240" cy="362" r="55"/>
      <circle class="bubble-ring" cx="178" cy="468" r="44"/>
    </svg>
    <div class="scroll-ornament" role="img" aria-label="Looping calligraphic scroll ornament crowning the grape cluster"></div>

    <div class="bubble typewriter b-king">King of<br>the red<br>wine</div>
    <div class="bubble typewriter b-grape">ca<br>bernet<br>sauvig<br>non</div>
    <div class="bubble slab b-vintage">
      <span class="label">VINTAGE<br>DATE</span>
      <span class="year">2013</span>
      <span class="note">GOOD YEAR</span>
    </div>
    <div class="bubble script b-sulfites">Contains<br>Sulfites</div>
    <div class="bubble typewriter b-cellared">Cellared<br>and bottled by<br>Tressaly Estate<br>Winery</div>
    <div class="bubble slab b-alc">
      <span class="label">ALC.</span>
      <span class="value">13,0%</span>
      <span class="note">BY VOL.</span>
    </div>
    <div class="bubble script b-motto">Nel Vino<br>C'è la<br>Verità</div>
    <div class="bubble b-pairing">Try Cabernet Sauvignon with a charred burger, a mushroom pizza or a slow marinated ribeye steak.</div>
    <div class="bubble typewriter b-fact">Cabernet<br>Sauvignon is<br>now the most<br>famous red wine<br>grape in the<br>world</div>
  </section>

</main>
</body>
</html>
```